Commercial janitorial cleaning

Janitorial cleaning particularly for commercial buildings. Website needs to specify free estimates. Location of service is Hudson, Valatie, East Greenbush, Troy, Albany ny area. Services page with Janitorial services- General Office Cleaning, Construction Cleaning, Carpet Extraction, Consultation/Business, Lighting Maintenance, Seasonal Deep Cleaning, Window cleaning, Event Cleaning, Floor and Carpet Cleaning, Floor Striping and Waxing. Contact us page with email phone number on page and a request page that emails me if they have any questions. About us page-the picture of my family on it with a section I can type a story myself.

Target Market(s)

Commercial businesses

Industry/Entity Type

Janitorial Service

Number of Pages Required

4 page

Font styles to use
Serif
Sans Serif
Script

Colors
ec1f27
1b1b1b
ffffff
9d9d9d

Requirements
Must have
• Phone number 555-314-2760. Must have free estimates on home page. Going for industrial / modern look to website
Nice to have
• Logo is a red and black building so if those colors could be coordinated to website that would be awesome.

```html
<!DOCTYPE html>
<html lang="en">
<head>
<meta charset="utf-8">
<title>Brightcrest Cleaning Services</title>
<link href="https://fonts.googleapis.com/css2?family=Open+Sans:ital,wght@0,400;0,600;0,700;1,400&family=Roboto:wght@500;700&family=Lato:wght@400;700&display=swap" rel="stylesheet">
<style>
:root{
  --red:#ec1f27;
  --ink:#1b1b1b;
  --white:#ffffff;
  --grey:#9d9d9d;
  --paper:#efefef;
  --black:#050505;
}
*{box-sizing:border-box;margin:0;padding:0}
html,body{width:1200px;height:2605px;overflow:hidden;background:var(--white)}
body{position:relative;font-family:"Open Sans",sans-serif;color:var(--ink)}
.abs{position:absolute}

/* header */
.site-header{position:absolute;left:0;top:0;width:1200px;height:133px;background:var(--white);border-bottom:3px solid var(--red)}
.brand{position:absolute;left:80px;top:44px;display:flex;align-items:center;gap:12px}
.brand-mark{width:34px;height:34px;background:var(--red)}
.brand-name{font-weight:700;font-size:17px;line-height:19px;color:var(--ink);width:170px}
.top-contact{position:absolute;top:26px;display:flex;align-items:center;gap:10px;font-size:13px;color:var(--ink)}
.top-contact .ico{width:28px;height:28px;border:2px solid var(--red);border-radius:50%;display:flex;align-items:center;justify-content:center}
.quote-btn{position:absolute;left:945px;top:22px;width:175px;height:34px;background:var(--red);color:var(--white);font-weight:700;font-size:15px;display:flex;align-items:center;justify-content:center}
.main-nav{position:absolute;left:395px;top:80px;width:805px;height:50px;background:var(--ink);clip-path:polygon(18px 0,100% 0,100% 100%,0 100%)}
.main-nav a{position:absolute;top:0;height:50px;line-height:50px;color:var(--white);font-weight:700;font-size:15px;text-decoration:none;text-align:center;width:150px}
.main-nav .sep{position:absolute;top:8px;width:1px;height:34px;background:#3b3b3b}
.main-nav .active{background:var(--red);top:8px;height:33px;line-height:33px;width:106px}

/* hero */
.hero{position:absolute;left:0;top:133px;width:1200px;height:475px;background:linear-gradient(90deg,#3a2d28 0%,#8a7b70 30%,#5c5048 60%,#9c8a3a 85%,#c9a72a 100%)}
.hero-caption{position:absolute;left:0;bottom:0;width:1200px;height:94px;background:rgba(20,20,20,.55);text-align:center;color:var(--white)}
.hero-caption h1{font-family:"Roboto",sans-serif;font-weight:700;font-size:25px;margin-top:18px;letter-spacing:.2px}
.hero-caption p{font-weight:600;font-size:24px;margin-top:4px}
.hero-arrow{position:absolute;top:177px;width:40px;height:40px;background:rgba(20,20,20,.85);display:flex;align-items:center;justify-content:center}

/* welcome */
.welcome{position:absolute;left:0;top:608px;width:1200px;height:429px;background:var(--paper)}
.welcome h2{position:absolute;left:80px;top:40px;font-size:31px;line-height:40px;font-weight:600;color:var(--ink)}
.welcome h2 span{color:var(--red)}
.rule{height:3px;width:60px;background:var(--red)}
.welcome p{position:absolute;left:80px;top:166px;width:627px;font-family:"Lato",sans-serif;font-size:14px;line-height:26px;color:var(--ink)}
.btn-red{background:var(--red);color:var(--white);font-weight:700;font-size:15px;display:flex;align-items:center;justify-content:center}
.team-photo{position:absolute;left:730px;top:62px;width:380px;height:367px;background:linear-gradient(180deg,#e9e6e3 0%,#c7b5a5 40%,#2b78b3 75%,#1e5f94 100%);border-radius:4px 4px 0 0}

/* services */
.services{position:absolute;left:0;top:1037px;width:1200px;height:768px;background:linear-gradient(135deg,#121212 0%,#1e1e1e 40%,#2a2412 65%,#181818 100%)}
.section-title{position:absolute;left:0;width:1200px;text-align:center;font-weight:700;font-size:31px}
.services .section-title{top:50px;color:var(--white)}
.section-title span{color:var(--red)}
.services .rule{position:absolute;left:570px;top:110px}
.svc{position:absolute;width:260px;text-align:center;color:var(--white);font-size:19px;line-height:25px}
.svc .glyph{width:54px;height:58px;margin:0 auto 14px;background:var(--red);border-radius:6px;opacity:.92}
.grid-h{position:absolute;left:80px;width:1040px;height:1px;background:rgba(255,255,255,.14)}
.grid-v{position:absolute;width:1px;background:rgba(255,255,255,.14)}

/* testimonials */
.testimonials{position:absolute;left:0;top:1805px;width:1200px;height:435px;background:var(--white)}
.testimonials .section-title{top:40px;color:var(--ink);font-weight:600}
.testimonials .rule{position:absolute;left:570px;top:98px}
.quote{position:absolute;left:160px;top:130px;width:950px;text-align:center;font-style:italic;font-size:14px;line-height:31px;color:var(--ink)}
.qmark{position:absolute;font-family:Georgia,serif;font-size:70px;color:#c9c9c9;line-height:1}
.divider{position:absolute;left:235px;top:242px;width:735px;height:1px;background:#d6d6d6}
.avatar{position:absolute;top:270px;width:72px;height:72px;border-radius:50%;background:linear-gradient(180deg,#d9d4cf,#8f8a86);border:3px solid #dcdcdc}
.avatar.current{border-color:var(--red);width:80px;height:80px;top:266px}
.client-name{position:absolute;left:0;top:358px;width:1200px;text-align:center;color:var(--red);font-size:19px}

/* footer */
.site-footer{position:absolute;left:0;top:2240px;width:1200px;height:313px;background:var(--black);color:var(--white)}
.site-footer h4{position:absolute;top:34px;font-size:15px;font-weight:700;letter-spacing:.3px}
.site-footer .rule{position:absolute;top:62px;width:34px;height:2px}
.quick-links{position:absolute;left:80px;top:88px;list-style:none;font-size:12px;line-height:33px}
.quick-links li::before{content:"›";color:var(--red);margin-right:4px}
.field{position:absolute;left:304px;width:248px;height:35px;border:1px solid #d0d0d0;font-size:11px;padding:9px 8px}
.submit{position:absolute;left:304px;top:2240px}
.contact-item{position:absolute;left:668px;display:flex;gap:10px;font-size:12px;line-height:15px}
.contact-item svg{flex:none;margin-top:1px}
.footer-brand{position:absolute;left:1000px;top:90px;width:130px;text-align:center;font-weight:700;font-size:16px;line-height:20px;color:#cfcfcf}
.social{position:absolute;top:215px;width:30px;height:30px;border-radius:50%;background:var(--red)}
.copyright{position:absolute;left:0;top:2553px;width:1200px;height:52px;background:var(--red);color:var(--white);font-size:12px;text-align:center;line-height:52px}
</style>
</head>
<body>

<header class="site-header">
  <div class="brand"><div class="brand-mark"></div><div class="brand-name">Brightcrest Cleaning Services</div></div>
  <div class="top-contact" style="left:530px">
    <span class="ico"><svg width="14" height="14" viewBox="0 0 24 24"><path fill="#ec1f27" d="M6.6 10.8a15 15 0 006.6 6.6l2.2-2.2c.3-.3.7-.4 1-.2 1.1.4 2.3.6 3.6.6.6 0 1 .4 1 1V20c0 .6-.4 1-1 1A17 17 0 013 4c0-.6.4-1 1-1h3.5c.6 0 1 .4 1 1 0 1.3.2 2.5.6 3.6.1.3 0 .7-.2 1z"/></svg></span>555-314-2760
  </div>
  <div class="top-contact" style="left:678px">
    <span class="ico"><svg width="14" height="14" viewBox="0 0 24 24"><path fill="#ec1f27" d="M3 6h18v12H3z"/><path fill="none" stroke="#fff" stroke-width="1.8" d="M3 6l9 7 9-7"/></svg></span>hello@brightcrestcleaning.com
  </div>
  <div class="quote-btn">Get A Free Quote</div>
  <nav class="main-nav">
    <a class="active" style="left:33px">HOME</a>
    <a style="left:193px">ABOUT US</a>
    <span class="sep" style="left:358px"></span>
    <a style="left:390px">SERVICES</a>
    <span class="sep" style="left:558px"></span>
    <a style="left:593px">CONTACT US</a>
  </nav>
</header>

<section class="hero" role="img" aria-label="Housekeeper making a bed in an office suite beside a yellow wet floor caution sign">
  <div class="hero-arrow" style="left:20px"><svg width="12" height="14" viewBox="0 0 12 14"><path d="M9 1L3 7l6 6" fill="none" stroke="#fff" stroke-width="2.4"/></svg></div>
  <div class="hero-arrow" style="left:1140px"><svg width="12" height="14" viewBox="0 0 12 14"><path d="M3 1l6 6-6 6" fill="none" stroke="#fff" stroke-width="2.4"/></svg></div>
  <div class="hero-caption">
    <h1>WE OFFER JANITORIAL CLEANING PARTICULARLY FOR COMMERCIAL BUILDINGS</h1>
    <p>Serving All of Hudson, Valatie, Troy &amp; Albany</p>
  </div>
</section>

<section class="welcome">
  <h2>WELCOME TO<br><span>BRIGHTCREST CLEANING SERVICES</span></h2>
  <div class="rule abs" style="left:80px;top:135px"></div>
  <p>Lorem ipsum dolor sit amet, consectetuer adipiscing elit, sed diam nonummy nibh euismod tincidunt ut laoreet dolore magna aliquam erat volutpat. Ut wisi enim ad minim veniam, quis nostrud exerci tation ullamcorper suscipit lobortis nisl ut aliquip ex ea commodo consequat. Duis autem vel eum iriure dolor in hendrerit in vulputate velit esse molestie consequat, vel illum dolore eu feugiat nulla facilisis at vero eros et accumsan et iusto odio dignissim qui blandit praesent luptatum zzril delenit augue duis dolore te feugait nulla facilisi.</p>
  <div class="btn-red abs" style="left:80px;top:350px;width:122px;height:34px">Read More</div>
  <div class="team-photo" role="img" aria-label="Two smiling cleaners in blue aprons giving a thumbs up beside a vacuum"></div>
</section>

<section class="services" aria-label="Our services">
  <h2 class="section-title">OUR <span>SERVICES</span></h2>
  <div class="rule"></div>

  <div class="grid-h" style="top:318px"></div>
  <div class="grid-h" style="top:515px"></div>
  <div class="grid-v" style="left:340px;top:162px;height:580px"></div>
  <div class="grid-v" style="left:600px;top:162px;height:580px"></div>
  <div class="grid-v" style="left:860px;top:162px;height:356px"></div>

  <div class="svc" style="left:80px;top:172px"><div class="glyph" role="img" aria-label="Office cleaning icon"></div>General<br>Office Cleaning</div>
  <div class="svc" style="left:340px;top:172px"><div class="glyph" role="img" aria-label="Construction cleaning icon"></div>Construction<br>Cleaning</div>
  <div class="svc" style="left:600px;top:172px"><div class="glyph" role="img" aria-label="Carpet extraction icon"></div>Carpet<br>Extraction</div>
  <div class="svc" style="left:860px;top:172px"><div class="glyph" role="img" aria-label="Consultation icon"></div>Consultation<br>/Business</div>

  <div class="svc" style="left:80px;top:368px"><div class="glyph" role="img" aria-label="Lighting maintenance icon"></div>Lighting<br>Maintenance</div>
  <div class="svc" style="left:340px;top:368px"><div class="glyph" role="img" aria-label="Floor waxing icon"></div>Floor Striping<br>and Waxing</div>
  <div class="svc" style="left:600px;top:368px"><div class="glyph" role="img" aria-label="Window cleaning icon"></div>Window<br>Cleaning</div>
  <div class="svc" style="left:860px;top:368px"><div class="glyph" role="img" aria-label="Event cleaning icon"></div>Event<br>Cleaning</div>

  <div class="svc" style="left:340px;top:566px"><div class="glyph" role="img" aria-label="Floor and carpet cleaning icon"></div>Floor and Carpet<br>Cleaning</div>
  <div class="svc" style="left:600px;top:566px"><div class="glyph" role="img" aria-label="Seasonal deep cleaning icon"></div>Seasonal<br>Deep Cleaning</div>
</section>

<section class="testimonials" aria-label="Client testimonials">
  <h2 class="section-title">CLIENT <span>TESTIMONIALS</span></h2>
  <div class="rule"></div>
  <span class="qmark" style="left:92px;top:116px">&ldquo;</span>
  <p class="quote">Lorem ipsum dolor sit amet, consectetuer adipiscing elit, sed diam nonummy nibh the is euismod tincidunt ut laoreet dolore magna aliquam erat volutpat. Ut wisi enim ad minim veniam, quis nostrud exerci tation ullamcorper suscipit lobortis nisl ut aliquip ex ea the commodo consequat. Duis autem vel eum iriure dolor in hendrerit in vulputate velit esse molestie consequat, vel illum dolore eu feugiat nulla</p>
  <span class="qmark" style="left:1032px;top:176px">&rdquo;</span>
  <div class="divider"></div>
  <svg class="abs" style="left:592px;top:242px" width="16" height="8"><path d="M0 0h16L8 8z" fill="#d6d6d6"/></svg>
  <div class="avatar" style="left:475px" role="img" aria-label="Client portrait"></div>
  <div class="avatar current" style="left:560px" role="img" aria-label="Client portrait"></div>
  <div class="avatar" style="left:652px" role="img" aria-label="Client portrait"></div>
  <div class="client-name">Lorem Ispum</div>
</section>

<footer class="site-footer">
  <h4 style="left:80px">QUICK LINKS</h4><div class="rule red" style="left:80px;background:var(--red)"></div>
  <ul class="quick-links"><li>Home</li><li>About us</li><li>services</li><li>Contact us</li></ul>

  <h4 style="left:302px">QUICK INQUIRY</h4><div class="rule" style="left:302px;background:var(--red)"></div>
  <div class="field" style="top:87px">Email</div>
  <div class="field" style="top:138px">Phone</div>
  <div class="field" style="top:188px">Message</div>
  <div class="btn-red abs" style="left:304px;top:240px;width:248px;height:34px">Submit</div>

  <h4 style="left:668px">CONTACT DETAILS</h4><div class="rule" style="left:668px;background:var(--red)"></div>
  <div class="contact-item" style="top:93px"><svg width="11" height="14" viewBox="0 0 12 16"><path fill="#ec1f27" d="M6 0a6 6 0 00-6 6c0 4.5 6 10 6 10s6-5.5 6-10a6 6 0 00-6-6zm0 8.5A2.5 2.5 0 116 3.5a2.5 2.5 0 010 5z"/></svg><div><b style="font-size:12px">Brightcrest Cleaning Services</b><br>Lorem Ipsum Helps You Lismarter,<br>Giving You Time To Focus-123</div></div>
  <div class="contact-item" style="top:163px"><svg width="13" height="13" viewBox="0 0 24 24"><path fill="#ec1f27" d="M6.6 10.8a15 15 0 006.6 6.6l2.2-2.2c.3-.3.7-.4 1-.2 1.1.4 2.3.6 3.6.6.6 0 1 .4 1 1V20c0 .6-.4 1-1 1A17 17 0 013 4c0-.6.4-1 1-1h3.5c.6 0 1 .4 1 1 0 1.3.2 2.5.6 3.6.1.3 0 .7-.2 1z"/></svg>555-314-2760</div>
  <div class="contact-item" style="top:201px"><svg width="13" height="13" viewBox="0 0 24 24"><path fill="#ec1f27" d="M5 8h14v11H5zM7 3h8l2 5H7z"/></svg>555-314-2760</div>
  <div class="contact-item" style="top:240px"><svg width="13" height="11" viewBox="0 0 24 18"><path fill="#ec1f27" d="M0 0h24v18H0z"/><path fill="none" stroke="#050505" stroke-width="2" d="M0 1l12 9 12-9"/></svg>hello@brightcrestcleaning.com</div>

  <div class="footer-brand">Brightcrest Cleaning Services</div>
  <span class="social" style="left:1015px" aria-label="Social link"></span>
  <span class="social" style="left:1052px" aria-label="Social link"></span>
  <span class="social" style="left:1089px" aria-label="Social link"></span>
</footer>

<div class="copyright">Copyright © 2017 Brightcrest Cleaning Services. All Rights Reserved.</div>

</body>
</html>
```